Modern Label for Loose Tea pouches on 4.5x6 Label

We need a new label for our teas that is very simple in design, but stylish and modern. This will be used to print labels for our loose tea pouches. The label will be at max 4.5x6 inches in size. There should be a place for the tea name, description, ingredients, and size that is changeable.
Preferably an AI file that allows me to setup variables to change the above items. There will also need to be our logo which is supplied, and our address on the label.
Address:
Brevo Leaf
846 Lower Maple Lane
Highland, NY 12617
Target Market(s)
Tea Lovers
Requirements
Must have
- Adobe Illustrator file with variables setup for replacement of tea name, description, ingredients, and size (weights 2oz, 4oz, 8oz, 1lb)

```html
<!DOCTYPE html>
<html lang="en">
<head>
<meta charset="utf-8">
<title>Brevo Leaf – Black Tea Label</title>
<link rel="stylesheet" href="https://fonts.googleapis.com/css2?family=Montserrat:wght@400&family=Playfair+Display:wght@400;700&display=swap">
<style>
  :root {
    --backdrop: #2b2e2f;
    --label-paper: #f3f3f2;
    --ink-teal: #1f5457;
    --ink-plum: #7c3a58;
  }
  * { margin: 0; padding: 0; box-sizing: border-box; }
  html, body {
    width: 1200px;
    height: 900px;
    overflow: hidden;
    background: var(--backdrop);
  }
  .canvas {
    position: relative;
    width: 1200px;
    height: 900px;
    display: flex;
    align-items: center;
    justify-content: center;
  }
  .tea-label {
    position: relative;
    width: 600px;
    height: 800px;
    background: var(--label-paper);
    padding: 0 96px;
  }
  .brand {
    position: absolute;
    top: 92px;
    left: 0;
    right: 0;
    display: flex;
    align-items: center;
    justify-content: center;
    gap: 10px;
  }
  .brand-dot {
    width: 12px;
    height: 12px;
  }
  .brand-name {
    font-family: "Playfair Display", serif;
    font-weight: 700;
    font-size: 26px;
    letter-spacing: 1px;
    color: var(--ink-plum);
  }
  .tea-name {
    position: absolute;
    top: 310px;
    left: 0;
    right: 0;
    text-align: center;
    font-family: "Montserrat", sans-serif;
    font-weight: 400;
    font-size: 47px;
    letter-spacing: 6px;
    color: var(--ink-teal);
  }
  .tea-description {
    position: absolute;
    top: 400px;
    left: 96px;
    right: 84px;
    font-family: "Playfair Display", serif;
    font-size: 14.5px;
    line-height: 17.6px;
    letter-spacing: 1px;
    color: var(--ink-plum);
  }
  .label-footer {
    position: absolute;
    top: 618px;
    left: 96px;
    right: 84px;
    display: flex;
    justify-content: space-between;
    font-family: "Playfair Display", serif;
    font-size: 14.5px;
    line-height: 19px;
    letter-spacing: 1.2px;
    color: var(--ink-teal);
  }
  .ingredients { text-align: right; }
  .net-weight {
    position: absolute;
    top: 752px;
    left: 0;
    right: 0;
    text-align: center;
    font-family: "Montserrat", sans-serif;
    font-size: 18px;
    letter-spacing: 1.5px;
    color: var(--ink-plum);
  }
</style>
</head>
<body>
  <main class="canvas">
    <section class="tea-label">
      <header class="brand">
        <svg class="brand-dot" viewBox="0 0 12 12" aria-hidden="true">
          <circle cx="6" cy="6" r="6" fill="var(--ink-plum)"/>
        </svg>
        <span class="brand-name">Brevo Leaf</span>
      </header>

      <h1 class="tea-name">BLACK TEA</h1>

      <p class="tea-description">Lorem ipsum dolor sit amet, consectetur adipiscing elit. Ut rhoncus lectus in ornare consequat. Donec blandit sem non elit euismod interdum. Aliquam quis quam mattis, lobortis nibh nec, porta turpis. Aliquam ullamcorper feugiat consectetur. Praesent volutpat turpis eget gravida viverra. Etiam eu tellus ut turpis posuere sagittis vel eu leo.</p>

      <footer class="label-footer">
        <address class="maker-address" style="font-style: normal;">
          Brevo Leaf<br>
          846 Lower Maple Lane<br>
          Highland, NY 12617
        </address>
        <div class="ingredients">
          ingredients:<br>
          posuere sagittis<br>
          vel eu leo
        </div>
      </footer>

      <p class="net-weight">200g</p>
    </section>
  </main>
</body>
</html>
```